Business card with logo and words.

Colours: aqua and white (but open to suggestions).
Double sided card ok.
Need to convey competence, calmness, listening skills
Words:
Quiet Harbour Care Planning
Rhoda Pemberton
RN, RM, MVRNB, Grad Dip Gr & Pall Care Couns, Grad Cert Pall Care in Aged Care
quietharbourcp@fernmail.example

```html
<!DOCTYPE html>
<html lang="en">
<head>
<meta charset="utf-8">
<title>Quiet Harbour Care Planning – Business Card</title>
<link rel="stylesheet" href="https://fonts.googleapis.com/css2?family=Montserrat:wght@700&family=Open+Sans:wght@400;600;700&display=swap">
<style>
  :root {
    --purple: #3b1f7b;
    --mint: #d0e7da;
    --white: #ffffff;
    --text-font: "Open Sans", Arial, sans-serif;
    --name-font: "Montserrat", Arial, sans-serif;
  }
  * { margin: 0; padding: 0; box-sizing: border-box; }
  html, body {
    width: 1034px;
    height: 1200px;
    overflow: hidden;
    background: var(--white);
  }
  .sheet {
    position: relative;
    width: 1034px;
    height: 1200px;
    background: var(--white);
  }
  .card-face {
    position: absolute;
    left: 0;
    width: 1034px;
    background: var(--mint);
    overflow: hidden;
  }
  .card-front { top: 0; height: 574px; }
  .card-back { top: 624px; height: 576px; }
  .wave {
    position: absolute;
    inset: 0;
    width: 100%;
    height: 100%;
  }
  .wave path { fill: var(--purple); }

  .emblem-area {
    position: absolute;
    left: 54px;
    top: 180px;
    width: 438px;
    height: 324px;
    border-radius: 28px;
    background: linear-gradient(160deg, rgba(255,255,255,0.95), rgba(208,231,218,0.85));
  }
  .brand-name {
    position: absolute;
    right: 60px;
    top: 380px;
    text-align: right;
    font-family: var(--text-font);
    font-weight: 700;
    font-size: 54px;
    line-height: 66px;
    color: var(--white);
  }

  .person-name {
    position: absolute;
    right: 68px;
    top: 172px;
    font-family: var(--name-font);
    font-weight: 700;
    font-size: 68px;
    line-height: 1;
    color: var(--purple);
    text-align: right;
  }
  .credentials {
    position: absolute;
    right: 34px;
    top: 274px;
    font-family: var(--text-font);
    font-weight: 400;
    font-size: 26px;
    line-height: 42px;
    color: var(--purple);
    text-align: right;
  }
  .email-bar {
    position: absolute;
    left: 36px;
    right: 0;
    top: 438px;
    height: 76px;
    background: linear-gradient(90deg, rgba(59,31,123,0) 0%, rgba(59,31,123,0.55) 22%, var(--purple) 45%, var(--purple) 100%);
    display: flex;
    align-items: center;
    justify-content: flex-end;
    padding-right: 40px;
  }
  .email {
    font-family: var(--text-font);
    font-weight: 600;
    font-size: 38px;
    color: var(--white);
    white-space: nowrap;
  }
</style>
</head>
<body>
<main class="sheet">
  <section class="card-face card-front">
    <svg class="wave" viewBox="0 0 862 478" preserveAspectRatio="none" aria-hidden="true">
      <path d="M0,45 C150,8 300,-8 420,12 C560,36 650,62 760,42 C810,32 840,16 862,6 L862,478 L0,478 Z"/>
    </svg>
    <div class="emblem-area" role="img" aria-label="Emblem illustration: an elderly couple with walking canes"></div>
    <p class="brand-name">Quiet Harbour<br>Care Planning</p>
  </section>

  <section class="card-face card-back">
    <svg class="wave" viewBox="0 0 862 480" preserveAspectRatio="none" aria-hidden="true">
      <path d="M0,0 L862,0 L862,18 C780,40 700,62 600,82 C480,106 380,62 260,72 C150,82 60,138 0,160 Z"/>
    </svg>
    <h1 class="person-name">Rhoda Pemberton</h1>
    <p class="credentials">
      RN, RM, MVRNB,<br>
      Grad Dip Gr &amp; Pall Care Couns,<br>
      Grad Cert Pall Care in Aged Care
    </p>
    <div class="email-bar">
      <span class="email">quietharbourcp@fernmail.example</span>
    </div>
  </section>
</main>
</body>
</html>
```